New Webpage for one of Ireland’s largest Asian Supermarket

Introduction to Lotus Pantry :

Lotus Pantry is one of the largest importer, retailer, wholesaler and distributor of asian food products in Ireland. We supply to the majority of asian restaurants, shops and take-aways in Ireland.
Restaurants, caterers and shops can take advantage of our delivery service where products are delivered throughout the Republic of Ireland using our dedicated fleet of vehicles.
For more than 30 years, Lotus Pantry has always adhered to the "customer first" policy sending our purchasing team to their places of origin to conduct investigations and to hire professionals to conduct assessments, to ensure that the most delicious and best quality products are provided to our customers.
Our stores stock more than 3,000 different kinds of commodities, mainly from Asia, including South Korea, Japan, mainland China, Hong Kong, Taiwan, Thailand, Malaysia and Vietnam, to meet the different tastes of our customers.

Job Description:
We would like to create a new look for our webpage in order to support multilingual feature and online shopping. The webpage can be in any CMS format, preferably wordpress.

Our current website is:
http://lotuspantry.example/

We hope to incorporate fun and creative designs in our new website.

This design project is to develop the website design concept which will:
# Give the user confidence that Lotus Pantry is a premier supermarket since 1981 and supplier to wholesalers and distributors. We provide a wide range of goods at good value.
# Inform the users of our online shopping service.
# Encourage the user to try our services.
# Looks fun, interesting, modern, respectable and trustworthy.

We are open to any fun or interesting ways of getting this message across to users.

We like the idea of real life images or cartoon based images embedded into the page similar to this:
http://www.copperkite.example/
http://www.mellowforge.example/
http://www.rvmeadows.example/
http://velmora.example/club/#reception
http://www.hadleyandquinn.example/index.php
http://www.pixelhive.example/

We like the online shopping feature similar to this :
http://www.roomdabs.example/

We like how they show their new products and brands they have at the end of their page:
http://themes.style.brisk-layouts.example/?isOpen=false&;t_r=true

But, ideas could be whatever you think will look good. Any interesting concepts are welcome.

Thank you for your interest. Please do not hesitate to email brendaq@lotuspantry.example should you have any queries about the contest and feel free to use any of our photos if necessary.
(our Chatterbook page : https://www.facebook.com/LotusPantry.example?ref=stream )

Requirements
Must have
• 1. Multilingual Feature (We will provide the content in different languages)
2. Online Shopping feature
3. When search in seekly, links of the subpages can also be shown as well as the homepage (please see attachment for example)
4. A search engine with similar design as http://www.roomdabs.example/
5. Emphasize promotion e.g. http://www.cartwell.example/WebShop/index.do#
6. Easy to manage and add new products onto the shopping page at the backend of the website
7. Chatterbook and chirpline link always on the right same as http://www.mellowforge.example/
7. At least one unique feature that you think we should have on our webpage
Nice to have
• 1. Blog
2. Embedded video
3. An area, perhaps in a corner to show whether we are open and online or not. When staff are available to deliver remote support the site should clearly show that staff are online working and available now to support. When we are offline the site should also show this. ( e.g. the chatbox in http://www.mellowforge.example/)
4. A webpage adaptable to portables, mobile phones etc.
5. Memorable slogans

```html
<!DOCTYPE html>
<html lang="en">
<head>
<meta charset="utf-8">
<title>Lotus Pantry – Home</title>
<link rel="stylesheet" href="https://fonts.googleapis.com/css2?family=Source+Sans+3:wght@400;600;700&display=swap">
<style>
:root{
  --black:#000;
  --white:#fff;
  --gold:#b8980a;
  --yellow:#ffe000;
  --text:#333;
  --muted:#444;
  --footer:#e6e6e5;
  --base:#3c3c3c;
  --blue:#1b4ba6;
  --side-fb:#2b6ab3;
  --side-tw:#2e9bd6;
  --chat:#e8786c;
}
*{box-sizing:border-box;margin:0;padding:0}
html,body{width:996px;height:1200px;overflow:hidden}
body{position:relative;background:var(--white);font-family:"Source Sans 3",sans-serif;color:var(--text)}
.abs{position:absolute}
a{color:inherit;text-decoration:none}

.site-header{left:0;top:0;width:996px;height:120px;background:var(--black)}
.brand{left:73px;top:44px;display:flex;align-items:center;gap:10px;color:var(--white);font-size:26px;font-weight:700}
.brand-mark{width:30px;height:30px;background:var(--yellow)}
.account-links{left:466px;top:35px;color:var(--white);font-size:13px;font-weight:600}
.account-links span{margin:0 10px}
.search{left:662px;top:32px;width:170px;height:22px;background:var(--white);border-radius:2px;font-size:11px;font-style:italic;color:#999;padding:4px 8px}
.search svg{position:absolute;right:6px;top:5px}
.lang{left:846px;top:31px;width:80px;height:23px;background:var(--white);border:1px solid #ccc;font-size:10px;padding:5px 5px;color:#222}
.lang .flag{position:absolute;left:32px;top:7px;width:18px;height:10px;background:#2b3f8c}
.lang svg{position:absolute;right:6px;top:8px}
.main-nav{left:465px;top:78px;display:flex;gap:31px;color:var(--white);font-size:14px;font-weight:600}
.main-nav .active{position:relative}
.main-nav .active::after{content:"";position:absolute;left:0;right:0;bottom:-8px;height:2px;background:var(--yellow)}

.hero{left:72px;top:148px;width:854px;height:254px;overflow:hidden}
.hero-photo{left:0;top:0;width:693px;height:254px;background:linear-gradient(90deg,#a8301c 0%,#c9c3a0 45%,#e3a514 70%,#f0b020 100%)}
.hero-edge{left:680px;top:0;width:14px;height:254px;background:#111}
.hero-side{left:694px;top:0;width:160px;height:254px;background:linear-gradient(90deg,#fff 0%,#b9bcc3 50%,#6d7a94 100%)}
.hours-tag{left:0;top:196px;width:193px;height:58px;background:rgba(20,20,20,.78);color:var(--white);font-size:12.5px;font-weight:600;line-height:21px;padding:7px 14px}
.dots{left:794px;top:233px;display:flex;gap:3px}
.dots i{width:9px;height:9px;border-radius:50%;border:1px solid #eee;background:#aaa}
.dots i:first-child{background:#fff}

.offer{width:249px}
.offer-frame{width:249px;height:151px;border:1px solid #ddd;padding:5px}
.offer-img{position:relative;width:237px;height:139px}
.offer-img .cap{position:absolute;left:0;bottom:0;width:100%;height:36px;background:rgba(255,255,255,.6);font-size:17px;color:#222;padding:7px 10px}
.offer h3{margin-top:8px;color:var(--gold);font-size:13.5px;font-weight:700}
.offer p{margin-top:6px;font-size:11px;line-height:22px;color:var(--muted)}

.blogs-title{left:71px;top:700px;font-size:17.5px;font-weight:600;color:#333}
.post{left:73px;width:510px}
.post h4{color:var(--gold);font-size:13.5px;font-weight:700}
.post p{margin-top:4px;font-size:11px;line-height:17.8px;color:#555}
.post .date{margin-top:4px;font-size:11px;font-weight:700;color:#333}
.video{left:623px;top:728px;width:304px;height:213px;background:linear-gradient(135deg,#7a6a5a,#c9c2b3 40%,#9a8a74 70%,#5a4e44)}
.video svg{position:absolute;left:126px;top:78px}

.site-footer{left:0;top:990px;width:996px;height:162px;background:var(--footer)}
.fcol{top:1003px;font-size:11.5px;color:#333}
.fcol h5{font-size:11.5px;font-weight:400;text-transform:uppercase;margin-bottom:8px}
.fcol li{list-style:none;line-height:24px}
.newsletter{left:586px;top:1001px}
.newsletter h5,.connect h5{font-size:13.5px;font-weight:400;color:#333}
.field{position:absolute;left:0;width:137px;height:26px;background:var(--white);font-size:11px;color:#666;padding:6px 8px}
.submit{position:absolute;left:75px;top:116px;width:62px;height:22px;background:var(--blue);color:var(--white);font-size:11px;text-align:center;line-height:22px}
.connect{left:788px;top:1001px}
.connect li{list-style:none;position:absolute;left:0;display:flex;align-items:center;gap:11px;font-size:13px;width:140px}
.connect li i{width:28px;height:28px;border-radius:4px}
.x4{left:958px;top:1073px;font-size:11px;color:#444}
.base{left:0;top:1152px;width:996px;height:48px;background:var(--base)}
.copy{left:72px;top:1174px;font-size:11.5px;color:#eee}
.chat-bar{left:771px;top:1173px;width:229px;height:31px;background:var(--chat);border:1px solid #c85e54;border-radius:3px 0 0 0;color:var(--white);font-size:10.5px;padding:8px 0 0 44px}
.chat-bar .menu{position:absolute;left:0;top:0;width:35px;height:29px;background:#f09c92}
.chat-bar svg{position:absolute;left:9px;top:9px}

.side-social{left:966px;width:30px;height:30px}
</style>
</head>
<body>

<header class="abs site-header">
  <a class="abs brand" href="#"><span class="brand-mark"></span>Lotus Pantry</a>
  <div class="abs account-links"><a href="#">My Account</a><span>::</span><a href="#">Cart (0) items</a></div>
  <div class="abs search">Search..
    <svg width="12" height="12" viewBox="0 0 12 12"><circle cx="5" cy="5" r="3.8" fill="none" stroke="#999" stroke-width="1.6"/><line x1="7.8" y1="7.8" x2="11" y2="11" stroke="#999" stroke-width="1.8"/></svg>
  </div>
  <div class="abs lang">ENG<span class="flag"></span>
    <svg width="10" height="6" viewBox="0 0 10 6"><path d="M0 0h10L5 6z" fill="#333"/></svg>
  </div>
  <nav class="abs main-nav">
    <a class="active" href="#">Home</a><a href="#">About Us</a><a href="#">Products</a><a href="#">Our Stores</a><a href="#">Events</a><a href="#">Contacts</a>
  </nav>
</header>

<section class="abs hero">
  <div class="abs hero-photo" role="img" aria-label="Store interior with rice posters and the shop name on an orange wall"></div>
  <div class="abs hero-edge"></div>
  <div class="abs hero-side" role="img" aria-label="Shop front entrance"></div>
  <div class="abs hours-tag">OPENING HOURS:<br>MON - SAT&nbsp; 9:00 - 14.00</div>
  <div class="abs dots"><i></i><i></i><i></i><i></i></div>
</section>

<article class="abs offer" style="left:71px;top:436px">
  <div class="offer-frame"><div class="offer-img" role="img" aria-label="Bowls of white rice at the market" style="background:linear-gradient(160deg,#2a3a3a,#e8e6e0 45%,#cfcac0 70%,#3a4a44)"><span class="cap">Sale -10% off on all</span></div></div>
  <h3>Vlputate velit esse molestie</h3>
  <p>Nunc venenatis lacinia lacus quis vulputate. Sus pendisse imperdiet leo sed urna molestie.</p>
</article>
<article class="abs offer" style="left:381px;top:436px">
  <div class="offer-frame"><div class="offer-img" role="img" aria-label="Fresh green salad with tomatoes" style="background:linear-gradient(150deg,#c7e07a,#5d9a2c 45%,#b8402a 75%,#7a3a5a)"><span class="cap">Flat 10% Off on all items</span></div></div>
  <h3>Nam liber tempor cum</h3>
  <p>Nunc venenatis lacinia lacus quis vulputate. Sus pendisse imperdiet leo sed urna molestie.</p>
</article>
<article class="abs offer" style="left:679px;top:436px">
  <div class="offer-frame"><div class="offer-img" role="img" aria-label="Fried dish with fresh herbs" style="background:linear-gradient(140deg,#f0c050,#c9772e 45%,#e8d9a0 70%,#6aa83a)"><span class="cap">Food Items 10% Off</span></div></div>
  <h3>Typi non habent legentis</h3>
  <p>Nunc venenatis lacinia lacus quis vulputate. Sus pendisse imperdiet leo sed urna molestie.</p>
</article>

<h2 class="abs blogs-title">Recent Blogs</h2>
<article class="abs post" style="top:737px">
  <h4>Suspendisse eu erat quam. Vivamus porttitor eros quis nisi lacinia sed.</h4>
  <p>Suspendisse eu erat quam. Vivamus porttitor eros quis nisi lacinia sed interdum lorem vulputate. Aliq uam a orci quis nisi sagittis sagittis. Etiam adipiscing, justo quis feugiat.Suspendisse eu erat quam. Viv amus porttitor eros quis nisi lacinia sed interdum lorem vulputate.</p>
  <p class="date">Posted on 02 June, 2013</p>
</article>
<article class="abs post" style="top:850px">
  <h4>Suspendisse eu erat quam. Vivamus porttitor eros quis nisi lacinia sed.</h4>
  <p>Suspendisse eu erat quam. Vivamus porttitor eros quis nisi lacinia sed interdum lorem vulputate. Aliq uam a orci quis nisi sagittis sagittis. Etiam adipiscing, justo quis feugiat.Suspendisse eu erat quam. Viv amus porttitor eros quis nisi lacinia sed interdum lorem vulputate.</p>
  <p class="date">Posted on 02 June, 2013</p>
</article>
<div class="abs video" role="img" aria-label="Video of store shelves stocked with packaged goods">
  <svg width="42" height="42" viewBox="0 0 42 42"><circle cx="21" cy="21" r="20" fill="#fff"/><path d="M15 11l15 10-15 10z" fill="#111"/></svg>
</div>

<footer class="abs site-footer"></footer>
<div class="abs fcol" style="left:75px"><h5>Company</h5><ul><li>About</li><li>Contact</li><li>Legals &amp; Privacy</li><li>Niptaiades Keuytaser</li><li>Nemosera Lasecaerat</li></ul></div>
<div class="abs fcol" style="left:260px"><h5>More</h5><ul><li>How it Works</li><li>FAQ</li><li>Media Centre</li><li>Suggest a Business</li><li>Blog</li></ul></div>
<div class="abs fcol" style="left:430px"><h5>Offer a Deal</h5><ul><li>Media Owners</li><li>Marketing Providers</li><li>Nemosera Lasecaerat</li><li>Binsequuntur</li><li>Dolar ipsum</li></ul></div>
<div class="abs newsletter"><h5>Newsletter Signup</h5>
  <div class="field" style="top:38px">Name</div>
  <div class="field" style="top:76px">Email Id</div>
  <div class="submit">SUBMIT</div>
</div>
<div class="abs connect"><h5>Connect with us</h5>
  <ul>
    <li style="top:35px"><i style="background:#2d4f8e"></i>Chatterbook</li>
    <li style="top:69px"><i style="background:#c4252c"></i>Pinwheelr</li>
    <li style="top:103px"><i style="background:#2ea3dc"></i>chirpline</li>
  </ul>
</div>
<div class="abs x4">X4</div>

<div class="abs base"></div>
<div class="abs copy">Copyrights 2013. All Rights Reserved.</div>
<div class="abs chat-bar"><span class="menu"></span>
  <svg width="18" height="12" viewBox="0 0 18 12"><rect y="0" width="18" height="2" fill="#fff"/><rect y="5" width="18" height="2" fill="#fff"/><rect y="10" width="18" height="2" fill="#fff"/></svg>
  Opening Hours : Mon - Sat&nbsp; 9.00 - 14.00
</div>

<a class="abs side-social" href="#" aria-label="Chatterbook" style="top:230px;background:var(--side-fb)"></a>
<a class="abs side-social" href="#" aria-label="chirpline" style="top:268px;background:var(--side-tw)"></a>

</body>
</html>
```